Weight loss surgery restaurant card

We need to create a card for patients who have undergone weight loss surgery to take to restaurants so they can request smaller meals. These patients have had surgery on their stomach so that they can only consume half to one cup of food at a time. So normal sized restaurant meals are way too big (and cost a lot). This card they can present to the restaurant to communicate the fact that they have had weight loss surgery and therefore request a smaller meal portion at reduced cost

Target Market(s)

Restaurants serving weight loss surgery patients

Industry/Entity Type

Health Care

Contact Information for Business Card

This will be a plastic card similar to business card size.

Requirements
Must have
• The front of the card should include the following text:
• The individual bearing this card has undergone weight loss surgery.
• This surgery restricts portion sizes to between half and one cup of food at a time.
• Please give consideration to allowing smaller portions of your regular meals to be ordered to reduce wastage and excess costs.
• Example: a half size portion priced at two thirds of usual cost.
• The back of the card will have spaces for the person to write certain information. These are the categories that can be filled in by hand:
• Name:
• Procedure performed:
• Date of procedure (month/year):
• Treating Clinic Name:
• Treating Clinic Signature:
• Somewhere down the bottom should be something along the lines of:
• supplied from marcuswheelan.com.au
Nice to have
• A nice design with imagery/colours etc ... not just the text on a white background! Bright attractive colours preferred.
• I have uploaded my logo ... a roughly triangular image followed by my name etc. The triangular logo image could be used somewhere on the card and this logo can be interchangeable for other clinics who purchase the card.
• **Please note that I don't want my name to be included as part of the logo on the card ... just use the triangular image on the side of the logo without the following name**
• Also, the colouring of the card does not have to reflect my logo colours as I am anticipating interchanging this logo with other logos if other clinics choose to adopt the card. I am interested to see other, more generic, colour choices as well as my logo colours

```html
<!DOCTYPE html>
<html lang="en">
<head>
<meta charset="utf-8">
<title>Weight Loss Surgery Restaurant Card</title>
<link rel="stylesheet" href="https://fonts.googleapis.com/css2?family=Urbanist:wght@400;500;700&display=swap">
<style>
  :root {
    --page-bg: #e9eaeb;
    --card-top: #2d2e30;
    --card-bottom: #1c1d1f;
    --teal: #3cbdb4;
    --teal-soft: rgba(60, 189, 180, 0.35);
    --grey-text: #8e9093;
    --panel: #cfd0d1;
    --panel-text: #5a5c5f;
    --panel-line: #8a8c8f;
  }
  * { box-sizing: border-box; margin: 0; padding: 0; }
  html, body {
    width: 1200px;
    height: 900px;
    overflow: hidden;
    background: var(--page-bg);
    font-family: "Urbanist", "Century Gothic", sans-serif;
  }
  .sheet {
    width: 1200px;
    height: 900px;
    display: flex;
    align-items: center;
    justify-content: center;
    gap: 40px;
  }
  .card {
    position: relative;
    width: 550px;
    height: 347px;
    border-radius: 22px;
    background: linear-gradient(160deg, var(--card-top), var(--card-bottom));
    box-shadow: 0 14px 30px rgba(0,0,0,0.28);
    overflow: hidden;
  }
  .card__pattern {
    position: absolute;
    right: -40px;
    bottom: -40px;
    width: 360px;
    height: 300px;
    background: radial-gradient(ellipse at 75% 70%, var(--teal-soft), rgba(60,189,180,0.08) 55%, transparent 75%);
  }

  /* Message side */
  .message {
    position: relative;
    padding: 30px 34px;
  }
  .message__lead,
  .message__key,
  .message__example {
    color: var(--teal);
    font-weight: 700;
    font-size: 21px;
    line-height: 1.18;
  }
  .message__note {
    color: var(--grey-text);
    font-size: 14.5px;
    line-height: 1.25;
    margin: 6px 0 10px;
  }
  .message__example { font-size: 18px; }

  /* Details side */
  .brand {
    position: absolute;
    left: 36px;
    top: 30px;
    display: flex;
    align-items: center;
    gap: 12px;
  }
  .brand__dot {
    width: 34px;
    height: 34px;
    border-radius: 50%;
    background: var(--teal);
  }
  .brand__name {
    color: var(--teal);
    font-size: 25px;
    font-weight: 500;
    letter-spacing: 0.06em;
    text-transform: uppercase;
    line-height: 1;
  }
  .brand__role {
    color: var(--grey-text);
    font-size: 9.5px;
    letter-spacing: 0.14em;
    text-transform: uppercase;
    margin-top: 4px;
  }
  .form-panel {
    position: absolute;
    left: 36px;
    top: 96px;
    width: 340px;
    height: 158px;
    background: var(--panel);
    border-radius: 10px;
    padding: 14px 18px;
    display: flex;
    flex-direction: column;
    justify-content: space-between;
  }
  .form-panel__field {
    display: flex;
    align-items: flex-end;
    gap: 4px;
    color: var(--panel-text);
    font-size: 12.5px;
  }
  .form-panel__line {
    flex: 1;
    border-bottom: 1px solid var(--panel-line);
    height: 12px;
  }
  .supplier {
    position: absolute;
    left: 36px;
    bottom: 30px;
  }
  .supplier__label {
    color: var(--grey-text);
    font-size: 13px;
  }
  .supplier__web {
    color: var(--teal);
    font-size: 15px;
    font-weight: 500;
  }
</style>
</head>
<body>
<main class="sheet">
  <section class="card card--message" aria-label="Card front">
    <div class="card__pattern" role="img" aria-label="Flowing dotted teal wave pattern"></div>
    <div class="message">
      <p class="message__lead">The individual bearing this card has undergone weight loss surgery.</p>
      <p class="message__note">Around 500,000 of these procedures are performed around the world every year.</p>
      <p class="message__key">This surgery restricts portion sizes to between half and one cup of food at a time.</p>
      <p class="message__note">Please give consideration to allowing smaller portions of your regular meals to be ordered to reduce wastage and excess costs.</p>
      <p class="message__example">Example: a half size portion priced at two thirds of usual cost.</p>
    </div>
  </section>

  <section class="card card--details" aria-label="Card back">
    <div class="card__pattern" role="img" aria-label="Flowing dotted teal wave pattern"></div>
    <div class="brand">
      <span class="brand__dot"></span>
      <div>
        <p class="brand__name">Marcus Wheelan</p>
        <p class="brand__role">General, Upper GI &amp; Bariatric Surgeon</p>
      </div>
    </div>
    <div class="form-panel">
      <p class="form-panel__field">Name:<span class="form-panel__line"></span></p>
      <p class="form-panel__field">Procedure performed:<span class="form-panel__line"></span></p>
      <p class="form-panel__field">Date of procedure (month/year):<span class="form-panel__line"></span></p>
      <p class="form-panel__field">Treating Clinic Name:<span class="form-panel__line"></span></p>
      <p class="form-panel__field">Treating Clinic Signature:<span class="form-panel__line"></span></p>
    </div>
    <div class="supplier">
      <p class="supplier__label">Purchased through</p>
      <p class="supplier__web">www.marcuswheelan.com.au</p>
    </div>
  </section>
</main>
</body>
</html>
```